Letter and Envelope Design For Juniper Crest Realty

Please design a letter and an envelope incorporating our logo (See Attached). We are also launched a business card contest. Since we want them to match, please feel free to submit a design for both the business card and also the letter design and envelope.

Requirements
Must have
• The envelope, the letter and the business cards must match somehow connecting the designs. We want them to have something that holds them together besides the logo.

```html
<!DOCTYPE html>
<html lang="en">
<head>
<meta charset="utf-8">
<title>Juniper Crest Realty – Stationery</title>
<link href="https://fonts.googleapis.com/css2?family=Source+Sans+3:wght@400;600&display=swap" rel="stylesheet">
<style>
  :root {
    --navy: #27307a;
    --ink: #4a4a4a;
    --charcoal: #3f3f3f;
    --charcoal-light: #4d4d4d;
    --paper: #ffffff;
    --backdrop: #e6e6e6;
  }
  * { box-sizing: border-box; margin: 0; padding: 0; }
  html, body { width: 1200px; height: 1200px; overflow: hidden; }
  body {
    position: relative;
    background: var(--backdrop);
    font-family: "Source Sans 3", sans-serif;
    color: var(--ink);
  }
  .piece { position: absolute; background: var(--paper); }

  /* Brand lockup */
  .brand { position: absolute; display: flex; flex-direction: column; align-items: center; transform: translateX(-50%); }
  .brand-ring { border-radius: 50%; border-style: solid; border-color: var(--navy); }
  .brand-name {
    color: var(--navy); font-weight: 600; text-transform: uppercase;
    text-align: center; line-height: 1.2; white-space: nowrap;
  }

  /* Contact rows */
  .contact-row { display: flex; align-items: center; white-space: nowrap; color: var(--ink); }
  .icon { display: inline-flex; align-items: center; justify-content: center; background: var(--navy); flex: none; }
  .icon svg { display: block; }

  /* Letterhead */
  .letter { left: 33px; top: 53px; width: 773px; height: 1084px; }
  .letter .brand { left: 386px; top: 37px; }
  .letter .brand-ring { width: 122px; height: 122px; border-width: 4px; }
  .letter .brand-name { font-size: 32px; letter-spacing: 4px; margin-top: 14px; }
  .letter-footer { position: absolute; left: 0; right: 0; top: 1012px; display: flex; flex-direction: column; align-items: center; gap: 12px; font-size: 13.5px; }
  .letter-footer .contact-line { display: flex; gap: 10px; }
  .letter-footer .icon { width: 18px; height: 18px; margin-right: 7px; }

  /* Business card – front */
  .card-front { left: 690px; top: 118px; width: 476px; height: 277px; }
  .card-front .brand { left: 108px; top: 87px; }
  .card-front .brand-ring { width: 66px; height: 66px; border-width: 3px; }
  .card-front .brand-name { font-size: 15px; letter-spacing: 2px; margin-top: 8px; }
  .card-front .divider { position: absolute; left: 212px; top: 48px; width: 1px; height: 174px; background: var(--ink); }
  .card-holder { position: absolute; left: 231px; top: 46px; }
  .card-holder .name { color: var(--navy); font-weight: 600; font-size: 18px; line-height: 1.1; }
  .card-holder .role { font-size: 14px; margin-top: 2px; }
  .card-front .contacts { position: absolute; left: 231px; top: 124px; display: flex; flex-direction: column; gap: 8px; font-size: 13.5px; }
  .card-front .icon { width: 18px; height: 18px; margin-right: 12px; }
  .edge-band { position: absolute; left: 0; right: 0; bottom: 0; height: 10px; background: var(--charcoal); }

  /* Business card – back */
  .card-back {
    left: 690px; top: 420px; width: 476px; height: 278px;
    background: radial-gradient(ellipse at 55% 45%, #565656 0%, var(--charcoal) 70%);
  }
  .card-back .brand { left: 232px; top: 64px; }
  .card-back .brand-ring { width: 110px; height: 110px; border-width: 4px; }
  .card-back .brand-name { color: var(--paper); font-size: 15px; letter-spacing: 2px; margin-top: 10px; }

  /* Envelope */
  .envelope { left: 622px; top: 725px; width: 544px; height: 329px; background: transparent; }
  .envelope-flap { position: absolute; left: 0; top: 0; }
  .envelope-body { position: absolute; left: 0; top: 72px; width: 544px; height: 257px; background: var(--paper); }
  .envelope .brand { left: 80px; top: 12px; }
  .envelope .brand-ring { width: 46px; height: 46px; border-width: 2.5px; }
  .envelope .brand-name { font-size: 11px; letter-spacing: 1.5px; margin-top: 6px; }
  .envelope .divider { position: absolute; left: 401px; top: 21px; width: 1px; height: 52px; background: var(--ink); }
  .envelope .contacts { position: absolute; left: 409px; top: 20px; display: flex; flex-direction: column; gap: 4.5px; font-size: 7.5px; }
  .envelope .icon { width: 10px; height: 10px; margin-right: 8px; }
  .envelope .edge-band { height: 7px; }
</style>
</head>
<body>

<svg width="0" height="0" style="position:absolute" aria-hidden="true">
  <defs>
    <symbol id="i-pin" viewBox="0 0 16 16"><path d="M8 2.5a3.5 3.5 0 0 0-3.5 3.5c0 2.6 3.5 6.5 3.5 6.5s3.5-3.9 3.5-6.5A3.5 3.5 0 0 0 8 2.5z" fill="none" stroke="#fff" stroke-width="1.2"/><circle cx="8" cy="6" r="1.2" fill="#fff"/></symbol>
    <symbol id="i-phone" viewBox="0 0 16 16"><path d="M2.5 6.5c0-2 2.5-3 5.5-3s5.5 1 5.5 3l-2.5.7-.6-1.5H5.1l-.6 1.5z" fill="#fff"/><rect x="4" y="8" width="8" height="4.5" rx="1" fill="#fff"/></symbol>
    <symbol id="i-mail" viewBox="0 0 16 16"><rect x="3" y="4.5" width="10" height="7" fill="none" stroke="#fff" stroke-width="1.2"/><path d="M3 4.5l5 4 5-4" fill="none" stroke="#fff" stroke-width="1.2"/></symbol>
    <symbol id="i-globe" viewBox="0 0 16 16"><g fill="none" stroke="#fff" stroke-width="1"><circle cx="8" cy="8" r="5"/><ellipse cx="8" cy="8" rx="2.2" ry="5"/><path d="M3 8h10M4 5.5h8M4 10.5h8"/></g></symbol>
  </defs>
</svg>

<!-- Letterhead -->
<section class="piece letter">
  <div class="brand">
    <div class="brand-ring"></div>
    <div class="brand-name">Juniper Crest Realty</div>
  </div>
  <footer class="letter-footer">
    <div class="contact-row"><span class="icon"><svg width="14" height="14"><use href="#i-pin"/></svg></span>Juniper Crest Realty</div>
    <div class="contact-line">
      <div class="contact-row"><span class="icon"><svg width="14" height="14"><use href="#i-phone"/></svg></span>312-555-0148</div>
      <div class="contact-row"><span class="icon"><svg width="14" height="14"><use href="#i-mail"/></svg></span>info@junipercrest-realty.com</div>
      <div class="contact-row"><span class="icon"><svg width="14" height="14"><use href="#i-globe"/></svg></span>www.junipercrest-realty.com</div>
    </div>
  </footer>
</section>

<!-- Business card front -->
<section class="piece card-front">
  <div class="brand">
    <div class="brand-ring"></div>
    <div class="brand-name">Juniper Crest Realty</div>
  </div>
  <div class="divider"></div>
  <div class="card-holder">
    <div class="name">Avery Lane</div>
    <div class="role">Realtor</div>
  </div>
  <div class="contacts">
    <div class="contact-row"><span class="icon"><svg width="14" height="14"><use href="#i-pin"/></svg></span>Juniper Crest Realty</div>
    <div class="contact-row"><span class="icon"><svg width="14" height="14"><use href="#i-phone"/></svg></span>312-555-0148</div>
    <div class="contact-row"><span class="icon"><svg width="14" height="14"><use href="#i-mail"/></svg></span>info@junipercrest-realty.com</div>
    <div class="contact-row"><span class="icon"><svg width="14" height="14"><use href="#i-globe"/></svg></span>www.junipercrest-realty.com</div>
  </div>
  <div class="edge-band"></div>
</section>

<!-- Business card back -->
<section class="piece card-back">
  <div class="brand">
    <div class="brand-ring"></div>
    <div class="brand-name">Juniper Crest Realty</div>
  </div>
</section>

<!-- Envelope -->
<section class="piece envelope">
  <svg class="envelope-flap" width="544" height="73" viewBox="0 0 544 73" aria-hidden="true">
    <defs>
      <radialGradient id="flap-shade" cx="50%" cy="40%" r="60%">
        <stop offset="0" stop-color="#5a5a5a"/>
        <stop offset="1" stop-color="#3f3f3f"/>
      </radialGradient>
    </defs>
    <path d="M0 73 L18 12 Q22 0 36 0 H508 Q522 0 526 12 L544 73 Z" fill="url(#flap-shade)"/>
  </svg>
  <div class="envelope-body">
    <div class="brand">
      <div class="brand-ring"></div>
      <div class="brand-name">Juniper Crest Realty</div>
    </div>
    <div class="divider"></div>
    <div class="contacts">
      <div class="contact-row"><span class="icon"><svg width="8" height="8"><use href="#i-pin"/></svg></span>Juniper Crest Realty</div>
      <div class="contact-row"><span class="icon"><svg width="8" height="8"><use href="#i-phone"/></svg></span>312-555-0148</div>
      <div class="contact-row"><span class="icon"><svg width="8" height="8"><use href="#i-mail"/></svg></span>info@junipercrest-realty.com</div>
      <div class="contact-row"><span class="icon"><svg width="8" height="8"><use href="#i-globe"/></svg></span>www.junipercrest-realty.com</div>
    </div>
    <div class="edge-band"></div>
  </div>
</section>

</body>
</html>
```